依頼詳細
<取扱商品>
レディースバレエシューズ・ルームシューズ・除菌スプレー・マスクケースなど

<ターゲット>
やや女性向け
基本は老若男女問わず

<使用画像について>
商品画像はコンペ終了後にお渡ししますので仮の画像を入れていただければと思います。
商品画像以外の使用素材は有料のものでも問題は有りませんが、quilva picsまたは低価格(0~2000円程度)のものでお願いします。
※もし有料素材を使う場合は最初から購入して頂く必要はないのでウォーターマーク付きのもので提案していただければ大丈夫です。

<デザイン>
明るめのやさしい感じでお願いします。
参考サイトほどピンクは強めでなくてもいいかと思いますが、デザイン次第では濃い色の使用もありかと思います。

参考サイト
https://pelrovin.jp/

<ページ幅>
1920pxでお願いします。

<特筆事項>
今回NIVOを使用するにあたりプラン的にNIVOマークが必須になります。
右上のテントのマークはありきでお願いします。

今後も定期的にデザインをお願いすることができる技量を持つ方を探しておりますので是非、単発と考えずにデザインを出していただければと思います。
それでは皆様のご応募よろしくお願い致します。
サイトURL
ページ数
1ページ
希望イメージ
シンプル 複雑
単色 カラフル
暗い 明るい
日常 高級
遊び心 厳粛
未来的 伝統的
女性的 男性的
希望する色
白・淡いピンク・淡い水色などの優しい色
納品ファイル
• フォトショップ形式 (.psd)
補足説明
■ 選んだ理由

こちらが想定した以上のデザインでした。

■ 提案者全員のお礼・コメント

この度は当方コンペにご提案いただきありがとうございました。
提案頂いた方々のデザインはどれも素敵なもので、真剣に吟味し当選者を選択させていただきました。
今後もミルトカを利用してのデザインコンペを行う予定ですので、残念ながら今回は当選とならなかった方もまたご参加いただけると幸いです。
今後もどうかよろしくお願い致します。

```html
<!DOCTYPE html>
<html lang="ja">
<head>
<meta charset="utf-8">
<title>Mirelle｜サスティナビリティ</title>
<link rel="stylesheet" href="https://fonts.googleapis.com/css2?family=Noto+Sans+JP:wght@300;400;500&family=Noto+Serif+JP:wght@400;500&family=Cormorant+Garamond:wght@500&display=swap">
<style>
:root{
  --bg:#ffffff;
  --text:#4a4446;
  --muted:#8a8285;
  --pink:#d7aab3;
  --pink-soft:#f3e6e8;
  --blush:#e9c9cf;
  --wood:#e8e2dc;
  --green:#6f9a5a;
  --card:#f7f1f1;
  --line:#d9d2d3;
  --white:#ffffff;
}
*{box-sizing:border-box;margin:0;padding:0}
html,body{width:1200px;height:2680px;overflow:hidden;background:var(--bg);color:var(--text);font-family:"Noto Sans JP",sans-serif}
.page{position:relative;width:1200px;height:2680px}

.site-header{position:absolute;top:0;left:0;width:1200px;height:56px;display:flex;align-items:center;justify-content:space-between;padding:0 36px;background:var(--white)}
.brand{font-family:"Noto Sans JP",sans-serif;font-weight:400;font-size:22px;letter-spacing:2px;color:var(--text)}
.main-nav{display:flex;gap:26px;align-items:center;font-size:12px;color:var(--text)}
.nav-icons{display:flex;gap:14px;margin-left:12px}

.hero{position:absolute;top:56px;left:0;width:1200px;height:664px;background:linear-gradient(120deg,#f2d9d6 0%,#e9e4de 30%,#ece6df 60%,#f0dcd7 85%,#f4ece0 100%)}
.hero-copy{position:absolute;left:0;right:0;top:250px;text-align:center}
.hero-title{font-family:"Noto Serif JP",serif;font-weight:500;font-size:38px;letter-spacing:6px;color:var(--text)}
.hero-sub{margin-top:18px;font-family:"Noto Serif JP",serif;font-size:15px;letter-spacing:3px;color:var(--text)}
.hero-sub em{font-style:normal;color:var(--green);font-size:22px}
.hero-arrow{position:absolute;right:24px;top:326px;width:36px;height:36px;border-radius:50%;background:rgba(255,255,255,.85);display:flex;align-items:center;justify-content:center}

.sdgs{position:absolute;top:820px;left:0;width:1200px;height:240px}
.sdgs-mark{position:absolute;left:230px;top:40px;width:240px;height:130px;background:linear-gradient(135deg,#2a8fc7,#3aa3d8)}
.sdgs-body{position:absolute;left:600px;top:38px;width:380px}
.sdgs-title{font-family:"Noto Serif JP",serif;font-weight:500;font-size:24px;color:#2f8fc4;letter-spacing:2px}
.sdgs-text{margin-top:20px;font-size:10.5px;line-height:2;color:var(--muted)}

.section-head{position:absolute;left:0;width:1200px;text-align:center}
.section-head h2{font-family:"Cormorant Garamond",serif;font-weight:500;font-size:28px;letter-spacing:3px}
.section-head p{font-size:9px;color:var(--muted);margin-top:2px}
.product-head{top:1150px}
.product-head::after{content:"";display:block;width:120px;height:1px;background:var(--line);margin:10px auto 0}

.product-grid{position:absolute;top:1250px;left:0;width:1200px;height:600px}
.tile{position:absolute}
.tile-label{position:absolute;width:180px;height:50px;left:50%;top:50%;margin:-25px 0 0 -90px;background:rgba(255,255,255,.85);display:flex;align-items:center;justify-content:center;font-size:12px;color:var(--text);letter-spacing:1px}
.tile-ballet{left:0;top:0;width:600px;height:600px;background:linear-gradient(180deg,#d8d8da 0%,#ece7e6 50%,#e3c9b9 100%)}
.tile-room{left:600px;top:0;width:600px;height:290px;background:linear-gradient(135deg,#e4c8cd,#c9a9b3 60%,#efe4e6)}
.tile-spray{left:600px;top:290px;width:300px;height:310px;background:linear-gradient(160deg,#cfd6d8,#8f9aa0 60%,#b9c3c6)}
.tile-mask{left:900px;top:290px;width:300px;height:310px;background:linear-gradient(160deg,#eadbe8,#cdb3d3 60%,#e8dde9)}
.tile-ballet .tile-label{top:70%}
.tile-mask .tile-label,.tile-spray .tile-label{width:140px;margin-left:-70px}

.more-btn{position:absolute;top:1890px;left:520px;width:160px;height:34px;border:1px solid var(--line);border-radius:17px;display:flex;align-items:center;justify-content:center;font-size:11px;letter-spacing:2px;background:var(--white);box-shadow:0 3px 6px rgba(0,0,0,.08)}

.guide{position:absolute;top:2090px;left:0;width:1200px;display:flex;justify-content:center;gap:160px}
.guide-item{width:160px;text-align:center}
.guide-item h3{font-family:"Cormorant Garamond",serif;font-weight:500;font-size:22px;letter-spacing:2px}
.guide-item p{font-size:9px;color:var(--muted)}
.guide-circle{margin:10px auto 0;width:150px;height:120px;border-radius:50%;background:var(--card);box-shadow:0 8px 14px rgba(0,0,0,.1);display:flex;align-items:center;justify-content:center}

.site-footer{position:absolute;top:2455px;left:0;width:1200px;height:225px;background:var(--pink);text-align:center;color:var(--white)}
.footer-links{margin-top:40px;font-size:10px;letter-spacing:1px}
.social{margin-top:28px;display:flex;justify-content:center;gap:12px}
.social span{width:18px;height:18px;border-radius:50%;background:var(--white);opacity:.9}
.footer-brand{margin-top:30px;font-size:20px;letter-spacing:2px}
.copyright{margin-top:8px;font-size:8px;opacity:.8}
</style>
</head>
<body>
<div class="page">
  <header class="site-header">
    <div class="brand">Mirelle</div>
    <nav class="main-nav">
      <span>商品一覧</span><span>会社概要</span><span>よくある質問</span><span>お問い合わせ</span>
      <span class="nav-icons">
        <svg width="14" height="14" viewBox="0 0 14 14" fill="none" stroke="#4a4446" stroke-width="1.2"><circle cx="7" cy="4.5" r="2.8"/><path d="M1.5 13c.5-3 3-4.5 5.5-4.5s5 1.5 5.5 4.5"/></svg>
        <svg width="16" height="14" viewBox="0 0 16 14" fill="none" stroke="#4a4446" stroke-width="1.2"><path d="M1 1h2.5l2 8h8l1.5-6H4.5"/><circle cx="6.5" cy="12" r="1"/><circle cx="12.5" cy="12" r="1"/></svg>
      </span>
    </nav>
  </header>

  <section class="hero" role="img" aria-label="木の板の上に置かれたピンクのバレエシューズと花の写真">
    <div class="hero-copy">
      <h1 class="hero-title">サスティナビリティ</h1>
      <p class="hero-sub">〜人と地球にやさしい<em>自然環境</em>を目指して〜</p>
    </div>
    <div class="hero-arrow"><svg width="10" height="12" viewBox="0 0 10 12" fill="none" stroke="#4a4446" stroke-width="1.5"><path d="M3 1l5 5-5 5"/></svg></div>
  </section>

  <section class="sdgs">
    <div class="sdgs-mark" role="img" aria-label="持続可能な開発目標のロゴ"></div>
    <div class="sdgs-body">
      <h2 class="sdgs-title">SDGsへの取り組み</h2>
      <p class="sdgs-text">私たちは日々の暮らしに寄り添う商品づくりを通して、環境と人にやさしい社会の実現を目指しています。素材の選定から製造、梱包、配送に至るまで、無駄を減らし長く使えるものをお届けします。これからも一人ひとりの毎日が心地よくなるよう、持続可能なものづくりに取り組んでまいります。地域や取引先の皆さまと協力し、未来へつながる活動を続けていきます。</p>
    </div>
  </section>

  <div class="section-head product-head"><h2>PRODUCT</h2><p>商品一覧</p></div>

  <section class="product-grid">
    <div class="tile tile-ballet" role="img" aria-label="トウで立つバレエシューズを履いた足の写真"><div class="tile-label">Ballet shoes</div></div>
    <div class="tile tile-room" role="img" aria-label="ビーズ刺繍のピンクのルームシューズの写真"><div class="tile-label">Room shoes</div></div>
    <div class="tile tile-spray" role="img" aria-label="除菌スプレーボトルの写真"><div class="tile-label">Spray</div></div>
    <div class="tile tile-mask" role="img" aria-label="ラベンダー色のマスクケースの写真"><div class="tile-label">Mask case</div></div>
  </section>

  <div class="more-btn">もっと見る</div>

  <section class="guide">
    <div class="guide-item"><h3>COMPANY</h3><p>会社概要</p>
      <div class="guide-circle"><svg width="18" height="24" viewBox="0 0 18 24" fill="#6a6265"><rect x="2" y="1" width="14" height="22" rx="1"/><rect x="5" y="5" width="3" height="3" fill="#f7f1f1"/><rect x="10" y="5" width="3" height="3" fill="#f7f1f1"/><rect x="5" y="11" width="3" height="3" fill="#f7f1f1"/><rect x="10" y="11" width="3" height="3" fill="#f7f1f1"/><rect x="7" y="17" width="4" height="6" fill="#f7f1f1"/></svg></div></div>
    <div class="guide-item"><h3>CONTACT</h3><p>お問い合わせ</p>
      <div class="guide-circle"><svg width="24" height="18" viewBox="0 0 24 18" fill="#6a6265"><rect x="1" y="1" width="22" height="16" rx="1"/><path d="M1.5 2l10.5 8 10.5-8" fill="none" stroke="#f7f1f1" stroke-width="1.5"/></svg></div></div>
    <div class="guide-item"><h3>FAQ</h3><p>よくある質問</p>
      <div class="guide-circle"><svg width="28" height="22" viewBox="0 0 28 22" fill="#6a6265"><path d="M1 1h16v11H7l-4 4v-4H1z"/><path d="M19 6h8v11h-2v4l-4-4h-9v-3h7z"/></svg></div></div>
  </section>

  <footer class="site-footer">
    <p class="footer-links">ご利用ガイド　｜　プライバシーポリシー</p>
    <div class="social"><span></span><span></span><span></span></div>
    <p class="footer-brand">Mirelle</p>
    <p class="copyright">© Mirelle All rights reserved.</p>
  </footer>
</div>
</body>
</html>
```